Stationery Design Project

We need a stationery design package for a new company based in Luxembourg called "Corvet Tax & Consulting" with a legal name "Corvet S.a.r.l.".

We are a personal tax compliance and consulting company specialising in Luxembourg, UK and US taxation.

We require a stationery package including the following:-

- letterhead/paper
- envelopes (C4, C5, DL)
- compliments slip
- business cards
- folder (A4 with two pockets)

We are looking for a modern, elegant design which remains professional.
Updates

Hi everyone, thank you for the designs so far - there are some that we do like so I have changed the status to non-refundable as we will definitely take one of them forwards.

I have today received the final logo files from the website designer so I will upload these shortly.  We are reviewing the designs to date tonight so will provide further feedback latest tomorrow morning.

Thanks again
Mirela

Industry/Entity Type

Business

Requirements
Must have
• The design should focus on the following main colour:-
#7D1935
and could use these two colours as accents, if required:-
#4A96AD
#F5F3EE

We have uploaded our logo which has been finalised 31 July 2013 (note I have deleted the previous logo files that were uploaded). I have uploaded jpg, png, psd files. I also have tif and eps but these are large in size so have not uploaded here - if you need them please let me know and I can upload.
Nice to have
• Business cards - we would like the business cards to be full main colour on one side. We are considering using a QR code on the business card to link to the website, but not a necessity.

Folder - we are considering including the company contact information preprinted on the inside right pocket instead of business cards

```html
<!DOCTYPE html>
<html lang="en">
<head>
<meta charset="utf-8">
<title>Corvet Tax &amp; Consulting – Business Cards</title>
<link rel="stylesheet" href="https://fonts.googleapis.com/css2?family=Open+Sans:wght@400;600&display=swap">
<style>
  :root {
    --maroon: #7D1935;
    --teal: #4A96AD;
    --cream: #F5F3EE;
    --white: #ffffff;
    --backdrop: #2b2b2b;
    --font: "Open Sans", sans-serif;
  }
  * { margin: 0; padding: 0; box-sizing: border-box; }
  html, body { width: 1200px; height: 900px; overflow: hidden; }
  body {
    background: var(--backdrop);
    font-family: var(--font);
    position: relative;
  }
  .card {
    position: absolute;
    top: 300px;
    width: 525px;
    height: 300px;
    overflow: hidden;
    box-shadow: 0 12px 30px rgba(0,0,0,0.45);
  }

  /* Front: full main colour */
  .card--front { left: 50px; background: var(--maroon); }
  .front-brand {
    position: absolute; left: 95px; top: 100px;
    display: flex; align-items: center; gap: 18px;
    color: var(--white);
  }
  .brand-dot {
    width: 70px; height: 70px; border-radius: 50%;
    border: 3px solid var(--white);
  }
  .brand-name {
    font-size: 40px; font-weight: 400; line-height: 1;
    letter-spacing: 1px;
  }
  .brand-sub {
    display: block; font-size: 16px; letter-spacing: 0.5px; margin-top: 4px;
  }
  .front-web {
    position: absolute; left: 0; right: 0; bottom: 30px;
    text-align: center; color: var(--white);
    font-size: 13px; letter-spacing: 5px;
  }

  /* Back: contact side */
  .card--back { left: 625px; background: var(--maroon); }
  .back-swoosh { position: absolute; left: 0; top: 0; width: 525px; height: 170px; }
  .back-brand {
    position: absolute; left: 30px; top: 35px;
    display: flex; align-items: center; gap: 12px;
    color: var(--maroon);
  }
  .back-brand .brand-dot { width: 50px; height: 50px; border: 3px solid var(--teal); }
  .back-brand .brand-name { font-size: 30px; }
  .back-brand .brand-sub { font-size: 12px; }
  .person {
    position: absolute; left: 28px; top: 165px; color: var(--white);
  }
  .person-name { font-size: 20px; color: var(--teal); font-weight: 400; }
  .person-role { font-size: 12px; margin-top: 2px; }
  .address { font-size: 13px; line-height: 1.45; margin-top: 18px; }
  .contact {
    position: absolute; left: 300px; top: 170px;
    font-size: 11.5px; line-height: 1.35; color: var(--white);
    list-style: none;
  }
  .contact-label { color: var(--teal); }
</style>
</head>
<body>

  <section class="card card--front" aria-label="Business card front">
    <div class="front-brand">
      <span class="brand-dot"></span>
      <span class="brand-name">CORVET<span class="brand-sub">TAX &amp; CONSULTING</span></span>
    </div>
    <p class="front-web">www.corvettax-consulting.com</p>
  </section>

  <section class="card card--back" aria-label="Business card back">
    <svg class="back-swoosh" viewBox="0 0 525 170" preserveAspectRatio="none" aria-hidden="true">
      <path d="M0 0 H525 V50 C420 110 220 145 0 150 Z" fill="var(--cream)"/>
      <path d="M0 150 C220 145 420 110 525 50 C430 118 230 158 0 162 Z" fill="var(--teal)"/>
      <path d="M110 158 L122 170 L134 157 Z" fill="var(--teal)"/>
    </svg>
    <div class="back-brand">
      <span class="brand-dot"></span>
      <span class="brand-name">CORVET<span class="brand-sub">TAX &amp; CONSULTING</span></span>
    </div>
    <div class="person">
      <h2 class="person-name">Dr. Helena Marsh</h2>
      <p class="person-role">Manager</p>
      <p class="address">Address 42 Rue Verte, 2210 Belair<br>L-1234 LUXEMBOURG</p>
    </div>
    <ul class="contact">
      <li><span class="contact-label">phone</span> 1 2480 311 604</li>
      <li><span class="contact-label">mobile:</span> 1 2480 311 604</li>
      <li><span class="contact-label">fax:</span> 1 2480 311 604</li>
      <li><span class="contact-label">email:</span> helena@corvettax-consulting.com</li>
      <li><span class="contact-label">website:</span> www.corvettax-consulting.com</li>
    </ul>
  </section>

</body>
</html>
```